wealth management firm, professional group, new model

we have a logo that works but we need a card, white background using our colors...clean look

our tag line if can be used in

The Bridge From Client to Owner

```html
<!DOCTYPE html>
<html lang="en">
<head>
<meta charset="utf-8">
<title>Veskaro Wealth Partners – Business Cards</title>
<link href="https://fonts.googleapis.com/css2?family=Montserrat:wght@400;500;600&display=swap" rel="stylesheet">
<style>
  :root {
    --navy: #1c2b4f;
    --navy-line: #22345c;
    --paper: #ffffff;
    --paper-line: #f3f3f3;
    --backdrop: #ffffff;
    --stage: #cfcfcf;
    --ink-soft: #3a4668;
  }
  * { margin: 0; padding: 0; box-sizing: border-box; }
  html, body { width: 1200px; height: 1200px; overflow: hidden; background: var(--backdrop); }
  body { position: relative; font-family: "Montserrat", sans-serif; }

  .card {
    position: absolute;
    overflow: hidden;
    box-shadow: 0 6px 14px rgba(0,0,0,0.28);
  }
  .card--front { background: var(--navy); color: var(--paper); }
  .card--back { background: var(--paper); color: var(--navy); }

  .card__band { position: absolute; left: 0; right: 0; height: 9px; }
  .card--front .card__band { background: var(--navy-line); }
  .card--back .card__band { background: var(--paper-line); }

  .wordmark { position: absolute; left: 0; right: 0; text-align: center; font-weight: 400; white-space: nowrap; }
  .wordmark__name { display: block; letter-spacing: 0.26em; padding-left: 0.26em; }
  .wordmark__sub { display: block; letter-spacing: 0.12em; padding-left: 0.12em; }

  /* top front card */
  .card--top-front { left: 53px; top: 48px; width: 524px; height: 340px; }
  .card--top-front .wordmark { top: 152px; }
  .card--top-front .wordmark__name { font-size: 44px; line-height: 1; }
  .card--top-front .wordmark__sub { font-size: 17px; margin-top: 15px; }

  /* back card */
  .card--top-back { left: 630px; top: 48px; width: 517px; height: 340px; }
  .card--top-back .wordmark { top: 40px; }
  .card--top-back .wordmark__name { font-size: 22px; line-height: 1; }
  .card--top-back .wordmark__sub { font-size: 8.5px; margin-top: 5px; color: var(--ink-soft); }

  .holder { position: absolute; left: 32px; top: 200px; }
  .holder__name { font-size: 16px; font-weight: 600; letter-spacing: 0.14em; }
  .holder__role { font-size: 12px; font-weight: 500; letter-spacing: 0.14em; margin-top: 6px; }

  .contact { position: absolute; top: 278px; font-size: 9.5px; line-height: 1.2; color: var(--ink-soft); font-style: normal; }
  .contact--left { left: 32px; }
  .contact--right { right: 23px; text-align: right; }

  /* presentation stage */
  .stage { position: absolute; left: 55px; top: 434px; width: 1092px; height: 713px; background: var(--stage); }
  .card--stage-front { left: 414px; top: 688px; width: 485px; height: 310px; }
  .card--stage-front .wordmark { top: 142px; }
  .card--stage-front .wordmark__name { font-size: 40px; line-height: 1; }
  .card--stage-front .wordmark__sub { font-size: 16px; margin-top: 12px; }
</style>
</head>
<body>
  <section class="card card--front card--top-front" aria-label="Business card front">
    <div class="card__band" style="top:80px"></div>
    <div class="card__band" style="top:262px"></div>
    <div class="wordmark">
      <span class="wordmark__name">VESKARO</span>
      <span class="wordmark__sub">WEALTH PARTNERS</span>
    </div>
  </section>

  <section class="card card--back card--top-back" aria-label="Business card back">
    <div class="card__band" style="top:92px"></div>
    <div class="card__band" style="top:325px"></div>
    <div class="wordmark">
      <span class="wordmark__name">VESKARO</span>
      <span class="wordmark__sub">WEALTH PARTNERS</span>
    </div>
    <div class="holder">
      <p class="holder__name">CARD HOLDER NAME</p>
      <p class="holder__role">CARD HOLDER POSITION</p>
    </div>
    <address class="contact contact--left">
      PHONE NUMBER<br>email@veskaro.example<br>veskaro.example
    </address>
    <address class="contact contact--right">
      ADDRESS1<br>address 2<br>ZIP CODE
    </address>
  </section>

  <div class="stage" aria-hidden="true"></div>

  <section class="card card--front card--stage-front" aria-label="Business card front, presentation view">
    <div class="card__band" style="top:68px"></div>
    <div class="card__band" style="top:250px"></div>
    <div class="wordmark">
      <span class="wordmark__name">VESKARO</span>
      <span class="wordmark__sub">WEALTH PARTNERS</span>
    </div>
  </section>
</body>
</html>
```